Email Signature

brightLoop Technology is in need of updating our email signature block. We are a technology firm that specializes in cloud services and infrastructure. We would like something that includes, name, title, office addresses (We currently have 3 locations), phone, cell, email and website. We are open to having a logo and motto and looking for something that we can roll out with the new year that is very eye catching.

Industry/Entity Type

Office

Font styles to use
Sans Serif

Requirements
Must have
• Employee name, title, office addresses (We currently have 3 locations), phone, cell, email and website

```html
<!DOCTYPE html>
<html lang="en">
<head>
<meta charset="utf-8">
<title>brightLoop Technology – Email Signature</title>
<link rel="stylesheet" href="https://fonts.googleapis.com/css2?family=Ubuntu:wght@400;500&family=Open+Sans:ital,wght@0,400;0,600;1,400&display=swap">
<style>
  :root {
    --bg: #ffffff;
    --green: #8cc63f;
    --blue: #1a8fce;
    --yellow: #f7d10f;
    --orange: #f26d21;
    --label-orange: #f06a1e;
    --heading-blue: #1a8fce;
    --text: #3d3d3d;
    --muted: #555555;
    --photo-light: #b7b9bb;
    --photo-dark: #6f7173;
  }
  * { box-sizing: border-box; margin: 0; padding: 0; }
  html, body {
    width: 1200px;
    height: 1000px;
    overflow: hidden;
    background: var(--bg);
  }
  .signature {
    position: absolute;
    left: 165px;
    top: 65px;
    display: grid;
    grid-template-columns: 420px 420px;
    grid-template-rows: 420px 420px;
    gap: 30px;
  }
  .tile {
    border: 12px solid;
    border-radius: 56px;
    background: var(--bg);
    display: flex;
    flex-direction: column;
  }
  .tile--photo { border-color: var(--green); align-items: center; justify-content: center; }
  .tile--contact { border-color: var(--blue); padding: 46px 30px 0 32px; }
  .tile--brand { border-color: var(--yellow); align-items: center; justify-content: center; }
  .tile--offices { border-color: var(--orange); padding: 52px 20px 0 22px; }

  .portrait {
    width: 272px;
    height: 308px;
    border-radius: 26px;
    background: linear-gradient(160deg, var(--photo-light), var(--photo-dark));
  }

  .person-name {
    font-family: "Ubuntu", sans-serif;
    font-weight: 400;
    font-size: 46px;
    color: var(--text);
    line-height: 1.1;
  }
  .person-title {
    font-family: "Open Sans", sans-serif;
    font-style: italic;
    font-size: 26px;
    color: var(--text);
    margin: 14px 0 22px;
  }
  .contact-list { list-style: none; }
  .contact-list li {
    font-family: "Open Sans", sans-serif;
    font-size: 21px;
    line-height: 40px;
    color: var(--muted);
    white-space: nowrap;
  }
  .contact-label { color: var(--label-orange); }

  .brand {
    display: flex;
    align-items: center;
    gap: 18px;
  }
  .brand-mark {
    width: 56px;
    height: 56px;
    background: var(--orange);
    border-radius: 6px;
  }
  .brand-name {
    font-family: "Ubuntu", sans-serif;
    font-weight: 400;
    font-size: 36px;
    line-height: 1.1;
    color: var(--text);
  }

  .office + .office { margin-top: 22px; }
  .office-name {
    font-family: "Open Sans", sans-serif;
    font-weight: 600;
    font-size: 20px;
    color: var(--heading-blue);
    line-height: 28px;
  }
  .office-address {
    font-family: "Open Sans", sans-serif;
    font-style: normal;
    font-size: 20px;
    line-height: 27px;
    color: var(--muted);
    white-space: nowrap;
  }
</style>
</head>
<body>
  <main class="signature">
    <section class="tile tile--photo">
      <div class="portrait" role="img" aria-label="Portrait photo of Mara Ellison"></div>
    </section>

    <section class="tile tile--contact">
      <h1 class="person-name">Mara Ellison</h1>
      <p class="person-title">Managing Director</p>
      <ul class="contact-list">
        <li><span class="contact-label">Phone:</span> 555-014-2210</li>
        <li><span class="contact-label">Cell:</span> 555-014-2210</li>
        <li><span class="contact-label">Email:</span> Contact@brightloopcorp.com</li>
        <li><span class="contact-label">Web:</span> www.brightloopcorp.com</li>
      </ul>
    </section>

    <section class="tile tile--brand">
      <div class="brand">
        <span class="brand-mark" aria-hidden="true"></span>
        <span class="brand-name">brightLoop<br>Technology</span>
      </div>
    </section>

    <section class="tile tile--offices">
      <div class="office">
        <h2 class="office-name">Corporate Office:</h2>
        <address class="office-address">2280 W. Cedar Mesa Road,<br>Suite 210, Scottsdale, AZ 85255</address>
      </div>
      <div class="office">
        <h2 class="office-name">Network Operating Center:</h2>
        <address class="office-address">940 S. 52nd St, Suite 1120,<br>Phoenix, AZ 85034</address>
      </div>
      <div class="office">
        <h2 class="office-name">Houston Office:</h2>
        <address class="office-address">415 Briar Park Avenue,<br>Suite 500, Houston, Texas, 77042</address>
      </div>
    </section>
  </main>
</body>
</html>
```